Clean professional design needed for landscape property business

We need a logo for a new lawncare, landscaping , property maintenance business called Fernway Grove.
Our services include lawn mowing, garden maintenance, clean ups and some property maintenance.
We want a double sided business card that is clean and very professional using the colour scheme from our logo which is provided.
the business card should have impact as we will use these to drop into people's letterboxes as a marketing drop.
Initially we want to see what you come up with so there is a very wide scope here to work with.

Project Deadline Extended
Reason: we feel our original deadline was too short. we have extended to give more time for quality submissions.

Target Market(s)

High end property owners who don't wish to do there own gardneing or property maintenance

Industry/Entity Type

Business

Contact Information for Business Card

Name
Postion/ Title
Phone number
mobile
web address
physical address

services offered

Font styles to use
Sans Serif

Requirements
Must have
• curved edges preferrred
Nice to have
• We like the idea of the logo being embossed or etched into the card so it looks like it is below the surface of the card
Should not have
• No stock images or characters.

```html
<!DOCTYPE html>
<html lang="en">
<head>
<meta charset="utf-8">
<title>Fernway Grove — Business Card</title>
<link href="https://fonts.googleapis.com/css2?family=Lato:wght@400;700&family=Montserrat:wght@500;700;800&display=swap" rel="stylesheet">
<style>
  :root {
    --page: #eceef2;
    --card: #ffffff;
    --green: #6abd45;
    --ink: #3d3d3f;
    --muted: #555558;
    --rule: #5a5a5d;
  }
  * { margin: 0; padding: 0; box-sizing: border-box; }
  html, body { width: 960px; height: 1200px; overflow: hidden; }
  body {
    background: var(--page);
    display: flex;
    flex-direction: column;
    align-items: center;
    justify-content: space-around;
    font-family: "Lato", sans-serif;
    color: var(--ink);
  }
  .card {
    position: relative;
    width: 700px;
    height: 400px;
    background: var(--card);
    border-radius: 18px;
    box-shadow: 0 10px 30px rgba(40, 50, 80, 0.14);
    overflow: hidden;
  }
  /* Front */
  .card-front .brand {
    position: absolute;
    left: 0; right: 0; top: 140px;
    display: flex;
    align-items: center;
    justify-content: center;
    gap: 18px;
  }
  .brand-name {
    font-family: "Lato", sans-serif;
    font-weight: 700;
    font-size: 56px;
    letter-spacing: -1px;
    color: var(--green);
  }
  .brand-mark {
    width: 26px; height: 26px;
    background: var(--green);
  }
  .card-front .address {
    position: absolute;
    left: 0; right: 0; top: 262px;
    text-align: center;
    font-size: 19px;
    color: var(--muted);
    letter-spacing: 0.3px;
  }
  /* Back */
  .card-back .brand-corner {
    position: absolute;
    right: 44px; top: 48px;
    display: flex;
    align-items: center;
    gap: 12px;
  }
  .card-back .brand-corner .brand-name { font-size: 34px; }
  .card-back .brand-corner .brand-mark { width: 18px; height: 18px; }
  .person {
    position: absolute;
    left: 48px; top: 150px;
  }
  .person-name {
    font-family: "Montserrat", sans-serif;
    font-weight: 800;
    font-size: 42px;
    letter-spacing: 0.5px;
    color: var(--ink);
  }
  .person-name .accent { color: var(--green); }
  .person-title {
    font-family: "Montserrat", sans-serif;
    font-weight: 500;
    font-size: 24px;
    letter-spacing: 1.5px;
    color: var(--ink);
    margin-top: 2px;
  }
  .rule {
    position: absolute;
    height: 1.5px;
    background: var(--rule);
  }
  .rule-top { left: 360px; right: 40px; top: 128px; }
  .rule-bottom { left: 40px; right: 360px; top: 286px; }
  .services {
    position: absolute;
    right: 44px; top: 150px;
    text-align: right;
    list-style: none;
    font-size: 20px;
    line-height: 1.35;
    color: var(--ink);
  }
  .contacts {
    position: absolute;
    left: 48px; top: 298px;
    list-style: none;
    font-size: 18px;
    line-height: 1.5;
    color: var(--ink);
  }
  .contacts li { display: flex; align-items: center; gap: 10px; }
  .contacts svg { width: 18px; height: 18px; flex: none; }
</style>
</head>
<body>
  <section class="card card-front" aria-label="Card front">
    <div class="brand">
      <span class="brand-name">Fernway Grove</span>
      <span class="brand-mark"></span>
    </div>
    <p class="address">4120 Larkspur Lane, Millbrook, PA 18240</p>
  </section>

  <section class="card card-back" aria-label="Card back">
    <div class="brand-corner">
      <span class="brand-name">Fernway Grove</span>
      <span class="brand-mark"></span>
    </div>
    <div class="rule rule-top"></div>
    <div class="person">
      <div class="person-name">ALEX <span class="accent">MORGAN</span></div>
      <div class="person-title">MANAGER</div>
    </div>
    <ul class="services">
      <li>First service goes here</li>
      <li>Second Service here</li>
      <li>Third Service here</li>
    </ul>
    <div class="rule rule-bottom"></div>
    <ul class="contacts">
      <li>
        <svg viewBox="0 0 18 18" aria-hidden="true"><circle cx="9" cy="9" r="9" fill="#6abd45"/><path d="M6 5.2c.4-.3.9-.2 1.1.2l.7 1.3c.2.4.1.8-.2 1l-.5.4c.4.9 1.1 1.6 2 2l.4-.5c.3-.3.7-.4 1-.2l1.3.7c.4.2.5.7.2 1.1l-.5.6c-.4.5-1.1.6-1.7.4-2-.8-3.6-2.4-4.4-4.4-.2-.6 0-1.3.4-1.7z" fill="#fff"/></svg>
        +1 215 555 0147
      </li>
      <li>
        <svg viewBox="0 0 18 18" aria-hidden="true"><circle cx="9" cy="9" r="9" fill="#6abd45"/><rect x="4.5" y="6" width="9" height="6.4" rx="0.8" fill="#fff"/><path d="M4.8 6.4 9 9.6l4.2-3.2" fill="none" stroke="#6abd45" stroke-width="1"/></svg>
        hello@fernwaygrove.com
      </li>
      <li>
        <svg viewBox="0 0 18 18" aria-hidden="true"><circle cx="9" cy="9" r="9" fill="#6abd45"/><circle cx="9" cy="9" r="4.6" fill="none" stroke="#fff" stroke-width="1.1"/><ellipse cx="9" cy="9" rx="2" ry="4.6" fill="none" stroke="#fff" stroke-width="1"/><path d="M4.4 9h9.2" stroke="#fff" stroke-width="1"/></svg>
        www.fernwaygrove.com
      </li>
    </ul>
  </section>
</body>
</html>
```